Echoes Across Ages

I need a book cover design for a world history book written for a target audience of high school students and progressive teachers. The book is more balanced towards a world history perspective than a Western-leaning perspective. The first 500 pages deal with the major turning points in world history - from the first hominids that roamed Africa to the end of the Cold War, and the final 100 pages cover the major challenges facing the world today. The book is 95% graphic details, hopefully-engaging stories and needed facts, but there is a bit of sarcasm, verbal irony and asides thrown in to keep the reader's eyes from glossing over. I would need a cover that would appeal to any school teacher, but something that would not scare off students or the average Joe off the street.
Updates

One added note, please leave the bottom right corner -  2" height by 3" width free of text/image for the ISBN code.

As far as a central image goes, it needs to be a dynamic (avoid something readers would readily see elsewhere in their lives) image, or nothing at all.  Also, please justify all text on the back cover to the left side (avoid centering).

Reason: A few people have voiced an interest in having the deadline extended through next weekend to allow for some alterations and also the ability to take advantage of the upcoming holidays. I will take you up on this request. Thank you all again for your submissions. i've seen some very unique takes on the story/tone of the book.

Industry/Entity Type

High School

Requirements
Must have
• I've enclosed a PDF with the text for the front and back cover.

On the back cover, I'd like the quote and the initial question to stand out. I'd like the initial question to be in lower case.

For the spine, I'd like the title font to match the title front from the front cover.

The book cover needs to measure 9.25" by 13.75" with a 1.5" spine. Allow .125 inches for the bleed.

I've attached a Word Document with all the text. The layout is just a suggestion.
Should not have
• I do not want any stock images that I'll need to pay for.

```html
<!DOCTYPE html>
<html lang="en">
<head>
<meta charset="utf-8">
<title>Echoes Across Ages – Book Cover</title>
<link href="https://fonts.googleapis.com/css2?family=Arimo:wght@400;700&display=swap" rel="stylesheet">
<style>
  :root {
    --back-base: #4e4d6c;
    --back-light: #6c6b8c;
    --back-dark: #34334c;
    --spine: #3b3a55;
    --rule: #0d0c14;
    --ink-light: #ffffff;
    --accent: #f3837c;
    --art-gold: #e6a93a;
    --art-blue: #3f8fcc;
    --art-night: #232034;
    --art-amber: #d79a2e;
  }
  * { margin: 0; padding: 0; box-sizing: border-box; }
  html, body {
    width: 1200px; height: 516px; overflow: hidden; background: #ffffff;
  }
  .cover {
    position: relative; width: 1200px; height: 516px; overflow: hidden;
    font-family: "Arimo", Arial, sans-serif; color: var(--ink-light);
  }

  /* Back cover */
  .back {
    position: absolute; left: 0; top: 0; width: 482px; height: 516px;
    background:
      radial-gradient(ellipse at 30% 25%, var(--back-light) 0%, transparent 55%),
      radial-gradient(ellipse at 75% 80%, var(--back-light) 0%, transparent 50%),
      linear-gradient(160deg, var(--back-base) 0%, var(--back-dark) 100%);
  }
  .back-question {
    position: absolute; left: 10px; top: 3px;
    font-size: 18px; line-height: 22px; color: var(--accent); font-weight: 400;
  }
  .back-copy {
    position: absolute; left: 16px; width: 450px;
    font-size: 13.6px; line-height: 17.8px; text-align: left;
  }
  .back-copy.intro { top: 43px; }
  .back-copy.middle { top: 169px; }
  .back-copy.closing { top: 311px; }
  .back-quote {
    position: absolute; left: 27px; top: 433px; width: 440px;
    font-size: 13.4px; line-height: 17.8px; color: var(--accent);
  }
  .back-quote .attribution { color: var(--ink-light); }

  /* Spine */
  .spine {
    position: absolute; left: 482px; top: 0; width: 120px; height: 516px;
    background: linear-gradient(180deg, #46445f 0%, var(--spine) 60%, #2f2e45 100%);
    border-left: 2px solid var(--rule); border-right: 1px solid var(--rule);
    text-align: center;
  }
  .spine-author {
    margin-top: 10px; font-size: 25px; line-height: 28px; font-weight: 400;
  }
  .spine-title {
    position: absolute; left: 50%; top: 90px; transform: translateX(-50%);
    writing-mode: vertical-lr; text-orientation: upright;
    font-size: 18px; letter-spacing: 2px; font-weight: 400;
  }

  /* Front cover */
  .front {
    position: absolute; left: 602px; top: 0; width: 598px; height: 516px;
  }
  .front-art {
    position: absolute; inset: 0; display: block;
  }
  .front-title {
    position: absolute; left: 226px; width: 200px; top: 4px;
    text-align: center; font-size: 37px; line-height: 48px; font-weight: 400;
  }
  .front-subtitle {
    position: absolute; left: 212px; width: 228px; top: 162px;
    text-align: center; font-size: 18px; line-height: 25px; font-weight: 400;
  }
  .front-author {
    position: absolute; left: 134px; top: 334px;
    font-size: 68px; line-height: 76px; white-space: nowrap; font-weight: 400;
  }
</style>
</head>
<body>
<div class="cover">

  <section class="back">
    <h2 class="back-question">do you have any idea how we got to here?</h2>
    <p class="back-copy intro">Well, if you’re like 97.4% of the people walking the planet, you haven’t got a clue. Sure, you might know a bit about a couple rivers in Mesopotamia, how some old philosopher wandered around the marketplace asking questions or how a cranky monk got ticked off one day and nailed a really long essay to the door of a church. But to be honest (and don’t be embarrassed), you’ve got some gaps.</p>
    <p class="back-copy middle">Be dense no more. In <em>Echoes Across Ages</em>, Daniel Marsh takes you through all the major tales, traditions and turning points of our world history - not just European history, but WORLD history. You’ll figure out real quick that the West might have had some crowning moments, but for the whole of the human history, it’s been the Persians, the Indians, the Chinese, the Muslims or some horse peoples from the steppe that have truly turned us into the clever little creatures we are today.</p>
    <p class="back-copy closing">And when most world history books fade off once the Cold War comes to a close, this sometimes cheekily-written tome just gets going. It finishes with a distinctively comprehensive look at the 21st century challenges facing the nine major regions of today’s world - Africa, Latin America, Japan, China, the Middle East, India, Russia, Europe and United States.</p>
    <blockquote class="back-quote">“Daniel Marsh expertly understands exactly what his audience wants to know, what they need to know. A page-turning account of our proudest achievements and our most colossal bumblings. It’s world’s history for the rest of us” <span class="attribution">- Tomas Ardell</span></blockquote>
  </section>

  <section class="spine">
    <div class="spine-author">Daniel<br>Marsh</div>
    <div class="spine-title">Echoes Across Ages</div>
  </section>

  <section class="front">
    <svg class="front-art" width="598" height="516" viewBox="0 0 598 516" role="img" aria-label="Painted artwork of two golden ancient sculpted figures side by side, in gold, bright blue and deep night tones">
      <defs>
        <linearGradient id="artTones" x1="0" y1="0" x2="1" y2="0">
          <stop offset="0" stop-color="var(--art-gold)"/>
          <stop offset="0.18" stop-color="var(--art-blue)"/>
          <stop offset="0.32" stop-color="var(--art-gold)"/>
          <stop offset="0.48" stop-color="var(--art-night)"/>
          <stop offset="0.72" stop-color="var(--art-night)"/>
          <stop offset="0.88" stop-color="var(--art-amber)"/>
          <stop offset="1" stop-color="var(--art-night)"/>
        </linearGradient>
        <linearGradient id="artShade" x1="0" y1="0" x2="0" y2="1">
          <stop offset="0" stop-color="#000" stop-opacity="0.1"/>
          <stop offset="1" stop-color="#000" stop-opacity="0.3"/>
        </linearGradient>
      </defs>
      <rect width="598" height="516" fill="url(#artTones)"/>
      <rect width="598" height="516" fill="url(#artShade)"/>
    </svg>
    <h1 class="front-title">Echoes Across Ages</h1>
    <p class="front-subtitle">The tales, traditions and turning points of world history and the regional challenges of today</p>
    <div class="front-author">Daniel Marsh</div>
  </section>

</div>
</body>
</html>
```